Vorla constructions

We are predominantly a residential home builder based in Melbourne, Victoria Australia. We construct houses, apartments, townhouses, multi-unit developments.

The name of the company is "Vorla Constructions"
My company believes in building unique construction projects mainly residential homes. The target customers are upmarket Melbourne residents/investors.

I want the brand name "Vorla" to be part of the logo. There's no need to put the word construction in the logo at this stage.

I would also like some ideas for a slogan e.g. "Just build it." or "We build quality homes." But I would like something unique and different for a slogan not the same old cliche.

vorlaconstructions-example.com.au
e: mdelton@vorlaconstructions-example.com.au
M: 0417836519
Address: 8/3 Marlow Close Clayton VIC 3168

Director:Mr Desmond Kellingworth

```html
<!DOCTYPE html>
<html lang="en">
<head>
<meta charset="utf-8">
<title>Vorla Constructions — Business Card</title>
<link rel="stylesheet" href="https://fonts.googleapis.com/css2?family=Oswald:wght@500;600&family=Poppins:wght@400;500&display=swap">
<style>
  :root {
    --page-bg: #1d1d22;
    --card-deep: #1b1433;
    --card-mid: #2b2050;
    --card-shade: #3a2c6b;
    --cyan: #1fb8e6;
    --cyan-faint: rgba(31, 184, 230, 0.16);
    --white: #ffffff;
    --soft-white: #d9d6e6;
  }
  * { box-sizing: border-box; margin: 0; padding: 0; }
  html, body {
    width: 1200px;
    height: 3000px;
    overflow: hidden;
    background: var(--page-bg);
  }
  .canvas {
    width: 1200px;
    height: 3000px;
    display: flex;
    flex-direction: column;
    align-items: center;
    justify-content: center;
    gap: 180px;
  }
  .card {
    position: relative;
    width: 1040px;
    height: 630px;
    border-radius: 44px;
    overflow: hidden;
    background: linear-gradient(150deg, var(--card-mid) 0%, var(--card-deep) 100%);
  }
  .card__art {
    position: absolute;
    inset: 0;
    width: 100%;
    height: 100%;
  }

  /* Front */
  .skyline {
    position: absolute;
    left: 40px;
    top: 40px;
    width: 520px;
    height: 590px;
    border-radius: 8px 8px 0 0;
    background: linear-gradient(180deg, var(--card-shade) 0%, var(--cyan) 100%);
  }
  .brand {
    position: absolute;
    left: 600px;
    top: 200px;
    color: var(--cyan);
    font-family: "Poppins", sans-serif;
    font-weight: 500;
    line-height: 1;
  }
  .brand__name {
    display: block;
    font-size: 132px;
    letter-spacing: 2px;
  }
  .brand__line {
    display: block;
    font-size: 44px;
    letter-spacing: 5px;
    margin-top: 10px;
  }

  /* Back */
  .back-mark {
    position: absolute;
    right: 60px;
    top: 310px;
    font-family: "Poppins", sans-serif;
    font-weight: 500;
    font-size: 120px;
    line-height: 1;
    color: var(--cyan-faint);
  }
  .person {
    position: absolute;
    left: 70px;
    top: 90px;
  }
  .person__name {
    font-family: "Oswald", sans-serif;
    font-weight: 600;
    font-size: 58px;
    letter-spacing: 1px;
    text-transform: uppercase;
    color: var(--white);
  }
  .person__role {
    font-family: "Poppins", sans-serif;
    font-weight: 400;
    font-size: 24px;
    letter-spacing: 3px;
    color: var(--cyan);
    margin-top: 4px;
  }
  .contact {
    position: absolute;
    left: 70px;
    top: 300px;
    list-style: none;
    display: flex;
    flex-direction: column;
    gap: 20px;
  }
  .contact__item {
    display: flex;
    align-items: center;
    gap: 18px;
    font-family: "Poppins", sans-serif;
    font-size: 22px;
    color: var(--soft-white);
  }
  .contact__icon {
    width: 26px;
    height: 26px;
    flex: none;
  }
</style>
</head>
<body>
<main class="canvas">

  <section class="card card--front" aria-label="Business card front">
    <div class="skyline" role="img" aria-label="Illustration of stylised building towers with a registered builder badge"></div>
    <div class="brand">
      <span class="brand__name">Vorla</span>
      <span class="brand__line">constructions</span>
    </div>
  </section>

  <section class="card card--back" aria-label="Business card back">
    <svg class="card__art" viewBox="0 0 1040 630" aria-hidden="true">
      <polygon points="560,630 1040,520 1040,560 720,630" fill="var(--cyan)"/>
      <polygon points="500,630 1040,505 1040,512 530,630" fill="var(--white)"/>
    </svg>
    <div class="back-mark" aria-hidden="true">Vorla</div>
    <div class="person">
      <h1 class="person__name">Desmond Kellingworth</h1>
      <p class="person__role">Director</p>
    </div>
    <ul class="contact">
      <li class="contact__item">
        <svg class="contact__icon" viewBox="0 0 24 24" aria-hidden="true"><path d="M6.6 10.8a15 15 0 0 0 6.6 6.6l2.2-2.2a1 1 0 0 1 1-.25 11.4 11.4 0 0 0 3.6.57 1 1 0 0 1 1 1V20a1 1 0 0 1-1 1A17 17 0 0 1 3 4a1 1 0 0 1 1-1h3.5a1 1 0 0 1 1 1c0 1.25.2 2.45.57 3.57a1 1 0 0 1-.25 1z" fill="var(--cyan)"/></svg>
        0417836519
      </li>
      <li class="contact__item">
        <svg class="contact__icon" viewBox="0 0 24 24" aria-hidden="true"><rect x="2" y="5" width="20" height="14" rx="2" fill="none" stroke="var(--cyan)" stroke-width="2"/><path d="M3 6l9 7 9-7" fill="none" stroke="var(--cyan)" stroke-width="2"/></svg>
        mdelton@vorlaconstructions-example.com.au
      </li>
      <li class="contact__item">
        <svg class="contact__icon" viewBox="0 0 24 24" aria-hidden="true"><circle cx="12" cy="12" r="9" fill="none" stroke="var(--cyan)" stroke-width="2"/><path d="M3 12h18M12 3c3 3 3 15 0 18M12 3c-3 3-3 15 0 18" fill="none" stroke="var(--cyan)" stroke-width="2"/></svg>
        www.vorlaconstructions-example.com.au
      </li>
      <li class="contact__item">
        <svg class="contact__icon" viewBox="0 0 24 24" aria-hidden="true"><path d="M12 2a7 7 0 0 0-7 7c0 5 7 13 7 13s7-8 7-13a7 7 0 0 0-7-7z" fill="var(--cyan)"/><circle cx="12" cy="9" r="2.5" fill="var(--card-deep)"/></svg>
        8/3 Marlow Close Clayton VIC 3168
      </li>
    </ul>
  </section>

</main>
</body>
</html>
```